Carla Vennet Independent Sales rep business card

I am and independent sales rep I currently rep 3 furniture lines and 1 art line
I need the logos of each line I represent on my business card
I would prefer to have one sided card but if it works better to have all logos on the back side then I will consider
If you need high res versions of logos please let me know asap
THX

Business

Carla Mosley Vennet
Independent Sales Rep
carla@vennetmail.com
555.418.6072

```html
<!DOCTYPE html>
<html lang="en">
<head>
<meta charset="utf-8">
<title>Carla Mosley Vennet — Business Card</title>
<link rel="stylesheet" href="https://fonts.googleapis.com/css2?family=Cinzel:wght@400;500&display=swap">
<style>
  :root {
    --backdrop: #2a2a2a;
    --card: #0b0b0b;
    --card-edge: #1c1c1c;
    --band: #151515;
    --silver: #d9d9d9;
    --silver-soft: #a8a8a8;
    --frame: #e6e6e6;
  }
  * { box-sizing: border-box; margin: 0; padding: 0; }
  html, body {
    width: 1200px;
    height: 900px;
    overflow: hidden;
    background: var(--backdrop);
  }
  .canvas {
    position: relative;
    width: 1200px;
    height: 900px;
    display: flex;
    align-items: center;
    justify-content: center;
  }
  .business-card {
    position: relative;
    width: 980px;
    height: 560px;
    background: linear-gradient(160deg, #161616 0%, var(--card) 55%, #050505 100%);
    border: 1px solid var(--card-edge);
    font-family: "Cinzel", serif;
    color: var(--silver);
  }
  .card-frame {
    position: absolute;
    inset: 26px;
    border: 2px solid var(--frame);
    display: flex;
    flex-direction: column;
    align-items: center;
  }
  .holder-name {
    margin-top: 62px;
    font-size: 44px;
    font-weight: 500;
    letter-spacing: 2px;
    color: #f2f2f2;
    line-height: 1;
  }
  .holder-role {
    margin-top: 8px;
    font-size: 25px;
    letter-spacing: 2px;
    color: var(--silver);
    line-height: 1;
  }
  .divider {
    position: relative;
    margin-top: 22px;
    width: 190px;
    height: 1px;
    background: var(--silver-soft);
  }
  .divider::after {
    content: "";
    position: absolute;
    left: 50%;
    top: 50%;
    width: 5px;
    height: 5px;
    background: var(--silver);
    border-radius: 50%;
    transform: translate(-50%, -50%);
  }
  .contact-email,
  .contact-phone {
    font-size: 19px;
    letter-spacing: 1px;
    color: var(--silver);
  }
  .contact-email { margin-top: 22px; }
  .contact-phone { margin-top: 14px; }
  .brand-band {
    position: absolute;
    left: 80px;
    right: 24px;
    bottom: 40px;
    height: 200px;
    background: linear-gradient(180deg, rgba(30,30,30,0) 0%, var(--band) 45%, var(--band) 100%);
    display: flex;
    align-items: flex-end;
    justify-content: space-between;
    padding: 0 30px 30px 20px;
  }
  .brand-line {
    font-family: "Cinzel", serif;
    font-size: 18px;
    font-weight: 400;
    letter-spacing: 2px;
    color: var(--silver-soft);
    display: flex;
    align-items: center;
    gap: 10px;
    white-space: nowrap;
  }
  .brand-line .mark {
    width: 10px;
    height: 10px;
    border-radius: 50%;
    background: var(--silver-soft);
  }
  .brand-line--lowest { margin-bottom: 0; }
  .brand-line--low { margin-bottom: 30px; }
  .brand-line--mid { margin-bottom: 60px; }
  .brand-line--high { margin-bottom: 90px; }
</style>
</head>
<body>
  <main class="canvas">
    <article class="business-card">
      <div class="card-frame">
        <h1 class="holder-name">Carla Mosley Vennet</h1>
        <p class="holder-role">Independent Sales Rep</p>
        <div class="divider"></div>
        <p class="contact-email">carla@vennetmail.com</p>
        <p class="contact-phone">555.418.6072</p>
      </div>
      <div class="brand-band">
        <span class="brand-line brand-line--lowest"><span class="mark"></span>Harlan Vos</span>
        <span class="brand-line brand-line--low">Marlow Ashe Home</span>
        <span class="brand-line brand-line--mid">Lise Moreau</span>
        <span class="brand-line brand-line--high">Orrin Vale Gallery</span>
      </div>
    </article>
  </main>
</body>
</html>
```